Korvell Plant Services

We are a heavy diesel mechanical business with additional air con certificates, remapping engine rebuilt

Contact Information for Business Card

Company Name, Director Name, Managing Director, Contact details, email and website

Font styles to use
Serif
Script

```html
<!DOCTYPE html>
<html lang="en">
<head>
<meta charset="utf-8">
<title>Korvell Plant Services – Business Card</title>
<link rel="stylesheet" href="https://fonts.googleapis.com/css2?family=Lato:wght@400;700&display=swap">
<style>
  :root {
    --bg: #4a4b4e;
    --bg-dark: #2a2b2e;
    --navy: #0b0a6e;
    --navy-deep: #05044f;
    --royal: #1a1ab8;
    --white: #ffffff;
    --ink: #0a0a0a;
  }
  * { box-sizing: border-box; margin: 0; padding: 0; }
  html, body { width: 1200px; height: 851px; overflow: hidden; }
  body {
    background: radial-gradient(ellipse at 55% 35%, var(--bg) 0%, var(--bg-dark) 100%);
    font-family: "Lato", sans-serif;
    position: relative;
  }
  .card {
    position: absolute;
    width: 540px;
    height: 309px;
    border-radius: 18px;
    overflow: hidden;
    box-shadow: 0 14px 30px rgba(0,0,0,0.45);
  }
  .card--back {
    left: 40px; top: 271px;
    background: linear-gradient(135deg, var(--navy) 0%, var(--navy-deep) 100%);
    display: flex; align-items: center; justify-content: center; gap: 14px;
  }
  .card--front { left: 620px; top: 271px; background: var(--navy); }
  .brand-mark {
    width: 26px; height: 26px; border-radius: 50%;
    background: var(--royal);
  }
  .brand-name {
    font-weight: 700; font-size: 30px; color: var(--royal);
    line-height: 1.1; letter-spacing: 0.5px;
  }
  .card--front .brand-name { color: var(--navy); font-size: 22px; }
  .card--front .brand-mark { background: var(--navy); width: 20px; height: 20px; }
  .front-shape { position: absolute; inset: 0; }
  .front-brand {
    position: absolute; left: 350px; top: 120px; width: 170px;
    display: flex; align-items: center; gap: 10px;
  }
  .contact {
    position: absolute; left: 30px; top: 58px; color: var(--white);
  }
  .contact__name {
    font-weight: 700; font-size: 25px; letter-spacing: 1px; text-transform: uppercase;
  }
  .contact__role { font-size: 15px; margin-top: 2px; }
  .contact__address { font-size: 12.5px; margin-top: 22px; line-height: 1.45; }
  .contact__list { list-style: none; margin-top: 14px; font-size: 13.5px; line-height: 1.55; }
  .contact__list li { display: flex; align-items: center; gap: 10px; }
  .contact__list svg { width: 13px; height: 13px; fill: var(--white); flex: none; }
</style>
</head>
<body>
  <section class="card card--back" aria-label="Card back">
    <span class="brand-mark"></span>
    <span class="brand-name">Korvell<br>Plant Services</span>
  </section>

  <section class="card card--front" aria-label="Card front">
    <svg class="front-shape" viewBox="0 0 540 309" preserveAspectRatio="none" aria-hidden="true">
      <defs>
        <linearGradient id="navyFade" x1="0" y1="0" x2="1" y2="1">
          <stop offset="0" stop-color="#1a1a8a"/>
          <stop offset="1" stop-color="#05044f"/>
        </linearGradient>
      </defs>
      <rect width="540" height="309" fill="url(#navyFade)"/>
      <path d="M325 -5 C 250 60, 250 250, 345 314" fill="none" stroke="#0a0a0a" stroke-width="6"/>
      <path d="M340 -5 C 268 60, 268 250, 360 314 L545 314 L545 -5 Z" fill="#ffffff"/>
    </svg>
    <div class="front-brand">
      <span class="brand-mark"></span>
      <span class="brand-name">Korvell<br>Plant Services</span>
    </div>
    <div class="contact">
      <h1 class="contact__name">Daniel Hartley</h1>
      <p class="contact__role">Managing Director</p>
      <p class="contact__address">27 Foundry Lane Works<br>Granton, Kent, UK, ME4 7QR</p>
      <ul class="contact__list">
        <li><svg viewBox="0 0 16 16"><path d="M3 1l3 3-2 2c1 2 3 4 5 5l2-2 3 3-2 3C6 15 1 10 0 3z"/></svg>(555) 014-2290</li>
        <li><svg viewBox="0 0 16 16"><path d="M4 0h8a1 1 0 011 1v14a1 1 0 01-1 1H4a1 1 0 01-1-1V1a1 1 0 011-1zm1 2v10h6V2z"/></svg>(555) 014-2291</li>
        <li><svg viewBox="0 0 16 16"><path d="M4 0h8v4H4zM1 5h14v7h-3v4H4v-4H1zM6 11v3h4v-3z"/></svg>(555) 014-2292</li>
        <li><svg viewBox="0 0 16 16"><path d="M0 3h16v10H0zm1 1l7 5 7-5z"/></svg>info@korvellplant.com</li>
        <li><svg viewBox="0 0 16 16"><circle cx="8" cy="8" r="7.5"/></svg>korvellplant.com</li>
      </ul>
    </div>
  </section>
</body>
</html>
```